Business Card for Coach - ready to print

Design Business Card ready to order prints www.lukasbrenner.coach

* An Overview / Background of the Business & Services
· Coaching
· Personal growth
* The Target Market / Audience you are trying to reach
· private person in different roles (self, familiy, business role)s
* Design Specifics; any preferences or ideas for Style, Colour, Imagery, etc
· See www.lukasbrenner.coach
· "simple" design
· (small) element of surprise / unusual element

* Information that will be placed in the Business Card
· Beratung und Coaching
· Address: Lukas Brenner, Talmatt 42, CH-8531 Winterthur, Mobile +41 76 254 63 07
* Do you have an existing website or Facebook page where designers can learn more about your company?
· lukasbrenner.coach

Target Market(s)

private person in different roles (self, familiy, business role)

Industry/Entity Type

Life Coaching

Contact Information for Business Card

Lukas Brenner
Talmatt 42
CH-8531 Winterthur

Mobile: +41 76 254 63 07
Email: lubr@sonnwelt.ch
www.lukasbrenner.coach

Font styles to use
Sans Serif

Colors

Designer to choose colors to be used in the design.

Requirements
Must have
• "simple" design
• element of surprise / unusual element
• Beratung & Coaching
• see www.lukasbrenner.coach for colors and so...
Nice to have
• TA Symbol (three rings on top of each other) - unsual presentation
• QR Code of Website (see if it fits in and still looks good).

```html
<!DOCTYPE html>
<html lang="en">
<head>
<meta charset="utf-8">
<title>Beratung and Coaching – Business Card</title>
<link href="https://fonts.googleapis.com/css2?family=Lato:wght@400;700;900&display=swap" rel="stylesheet">
<style>
  :root {
    --backdrop: #2b2b2d;
    --card: #141415;
    --accent: #5cc3ec;
    --text-light: #e9e9e9;
    --text-muted: #8d8d8f;
    --rule: #4a4a4c;
    --photo-top: #b9bcc0;
    --photo-bottom: #6f747b;
  }
  * { box-sizing: border-box; margin: 0; padding: 0; }
  html, body {
    width: 1200px; height: 1108px; overflow: hidden;
    background: var(--backdrop);
    font-family: "Lato", sans-serif;
  }
  .sheet {
    position: relative; width: 1200px; height: 1108px;
    display: flex; justify-content: center; align-items: center; gap: 60px;
  }
  .card {
    position: relative; width: 440px; height: 660px;
    background: var(--card); border-radius: 18px;
    box-shadow: 0 14px 30px rgba(0,0,0,.45);
    text-align: center;
  }
  .portrait {
    position: absolute; left: 50%; transform: translateX(-50%);
    width: 236px; height: 236px; border-radius: 50%;
    border: 2px solid var(--accent);
    background: radial-gradient(circle at 50% 35%, var(--photo-top), var(--photo-bottom));
  }
  .card--front .portrait { top: 104px; }
  .card--back .portrait { top: 118px; }

  .name {
    position: absolute; top: 368px; left: 0; right: 0;
    font-weight: 900; font-size: 36px; letter-spacing: .5px;
    color: var(--accent);
  }
  .role {
    position: absolute; top: 412px; left: 0; right: 0;
    font-size: 19px; color: var(--text-light);
  }
  .icon-row {
    position: absolute; top: 446px; left: 70px; right: 70px;
    display: flex; align-items: center; gap: 6px;
  }
  .icon-row .rule { flex: 1; height: 1px; background: var(--rule); }
  .icon-row svg { width: 24px; height: 24px; display: block; }
  .contacts {
    position: absolute; top: 484px; left: 0; right: 0;
    font-size: 19px; line-height: 27px; color: var(--text-muted);
  }
  .divider {
    position: absolute; top: 574px; left: 100px; right: 100px;
    height: 1px; background: var(--rule);
  }
  .address {
    position: absolute; top: 584px; left: 0; right: 0;
    font-size: 18px; line-height: 23px; color: var(--text-muted);
  }
  .address .business { color: var(--accent); }

  .tagline {
    position: absolute; top: 388px; left: 0; right: 0;
    font-size: 31px; color: var(--accent);
  }
  .services {
    position: absolute; top: 518px; left: 0; right: 0;
  }
  .services h2 {
    font-weight: 900; font-size: 25px; color: var(--accent); letter-spacing: .5px;
  }
  .services .rule {
    width: 150px; height: 1px; background: var(--rule); margin: 8px auto 10px;
  }
  .services li {
    list-style: none; font-size: 21px; line-height: 27px; color: var(--text-muted);
  }
</style>
</head>
<body>
<main class="sheet">
  <section class="card card--front">
    <div class="portrait" role="img" aria-label="Portrait photo of the coach"></div>
    <h1 class="name">JONAS MEIER</h1>
    <p class="role">Founder | CEO</p>
    <div class="icon-row">
      <span class="rule"></span>
      <svg viewBox="0 0 24 24" aria-label="Phone"><circle cx="12" cy="12" r="12" fill="var(--accent)"/><path d="M8.6 6.5l1.8 2.6-1.1 1.3c.7 1.6 2 2.9 3.6 3.6l1.3-1.1 2.6 1.8-1 2c-4.7-.4-8.6-4.3-9-9z" fill="var(--card)"/></svg>
      <svg viewBox="0 0 24 24" aria-label="Email"><circle cx="12" cy="12" r="12" fill="var(--accent)"/><rect x="6" y="8" width="12" height="8.5" fill="none" stroke="var(--card)" stroke-width="1.4"/><path d="M6 8l6 5 6-5" fill="none" stroke="var(--card)" stroke-width="1.4"/></svg>
      <svg viewBox="0 0 24 24" aria-label="Website"><circle cx="12" cy="12" r="12" fill="var(--accent)"/><g fill="none" stroke="var(--card)" stroke-width="1.3"><circle cx="12" cy="12" r="6.2"/><ellipse cx="12" cy="12" rx="2.8" ry="6.2"/><path d="M5.8 12h12.4M6.8 9h10.4M6.8 15h10.4"/></g></svg>
      <span class="rule"></span>
    </div>
    <p class="contacts">+41 76 254 63 07<br>lubr@sonnwelt.ch<br>www.lukasbrenner.coach</p>
    <div class="divider"></div>
    <p class="address"><span class="business">Beratung and Coaching</span><br>Lukas Brenner, Talmatt 42<br>CH-8531 Winterthur</p>
  </section>

  <section class="card card--back">
    <div class="portrait" role="img" aria-label="Portrait photo of the coach"></div>
    <p class="tagline">Beratung and Coaching</p>
    <div class="services">
      <h2>SERVIES:</h2>
      <div class="rule"></div>
      <ul>
        <li>Coaching</li>
        <li>Personal growth</li>
      </ul>
    </div>
  </section>
</main>
</body>
</html>
```